One Pager Website for various security awareness videos

We need a one pager website (design & coding) for our security awareness video series. We imagine placing a few (3-4 sample videos) on the website, a customer referal and some contact form. SOmething similar to https://quorvel.com/watch-now/. Here are some of the videos which we will place on the website:
https://www.streamdeck-example.net/watch?v=Hq7PzkA2mLd&t=112s
https://www.streamdeck-example.net/watch?v=Vb3RkeWn8Ts
https://www.streamdeck-example.net/watch?v=Jw9CdpLr4Ya
https://www.streamdeck-example.net/watch?v=Tz6GyqBn2Kx
https://www.streamdeck-example.net/watch?v=Rm4XhaPe7Qu
https://www.streamdeck-example.net/watch?v=Ed8WokSj3Lf
https://www.streamdeck-example.net/watch?v=Ny2BquTc5Hv
https://www.streamdeck-example.net/watch?v=Pk5FsmVd9Ga
https://www.streamdeck-example.net/watch?v=Wc7JteHn3Rb
As for logo: our company www.tembrashield.com is the creator of those videos. You can use our logo / name.
Target Market(s)
B2B security officers in large enterprises
Coding
Coded - Design and coding required
Number of Pages Required
1 page
Look and feel

```html
<!DOCTYPE html>
<html lang="en">
<head>
<meta charset="utf-8">
<title>Tembra Shield — Video Library</title>
<link href="https://fonts.googleapis.com/css2?family=Montserrat:ital,wght@0,400;0,500;0,600;0,700;0,800;1,400&display=swap" rel="stylesheet">
<style>
:root{
  --orange:#f9a51a;
  --hero-teal:#1aaeb7;
  --section-teal:#0b97a0;
  --bright-teal:#00b4c0;
  --footer-teal:#06b2bd;
  --social-dot:#0a8f98;
  --ink:#2b2b2b;
  --text:#555;
  --light:#f6f6f6;
  --white:#fff;
}
*{margin:0;padding:0;box-sizing:border-box}
html,body{width:1200px;height:3002px;overflow:hidden}
body{font-family:'Montserrat',sans-serif;color:var(--ink);background:var(--light);position:relative}
.abs{position:absolute}
/* hero */
.hero{position:absolute;left:0;top:0;width:1200px;height:400px;background:#f1f1f1}
.hero-panel{position:absolute;left:0;top:0;width:516px;height:400px;background:var(--hero-teal)}
.brand{position:absolute;display:flex;align-items:center;gap:8px;font-weight:800;font-size:26px;color:#1d1d1d}
.brand-dot{width:28px;height:28px;border-radius:50%;background:var(--orange)}
.hero-title{left:88px;top:180px;font-size:31px;font-weight:700;color:var(--white)}
.hero-sub{left:88px;top:226px;width:400px;font-size:19.5px;line-height:24px;color:var(--white);text-transform:uppercase}
.nav{position:absolute;left:722px;top:53px;display:flex;gap:24px;font-size:14px;color:#333}
.nav span{display:flex;align-items:center;gap:4px}
.hero-art{left:606px;top:93px;width:490px;height:290px;border-radius:8px;background:radial-gradient(circle at 50% 40%,#dbe9ee,#eeeeee 70%)}
/* intro */
.intro-thumb{left:88px;top:479px;width:496px;height:400px;border-radius:6px;overflow:hidden;background:linear-gradient(100deg,#fbb21f 0 42%,#55698a 42% 100%)}
.play-big{position:absolute;left:204px;top:152px;width:92px;height:92px;border-radius:50%;background:var(--orange);border:6px solid rgba(255,255,255,.25);display:flex;align-items:center;justify-content:center}
.intro-title{left:648px;top:533px;font-size:25px;font-weight:700;color:#333}
.intro-text{left:648px;top:587px;width:448px;font-size:15.5px;line-height:24px;color:var(--text)}
.btn{position:absolute;background:var(--orange);color:var(--white);font-weight:700;font-size:11.5px;border-radius:16px;display:flex;align-items:center;justify-content:center}
/* popular */
.popular{position:absolute;left:0;top:959px;width:1200px;height:1327px;background:var(--section-teal)}
.sec-title{position:absolute;left:0;width:1200px;text-align:center;font-size:25px;font-weight:700;color:var(--white)}
.acc{position:absolute;left:88px;width:1024px;height:48px;border-radius:3px;background:var(--orange);color:var(--white);font-weight:700;font-size:16px;display:flex;align-items:center;justify-content:space-between;padding:0 22px}
.acc.open{background:var(--bright-teal)}
.acc-icon{width:16px;height:16px;border:1.5px solid var(--white);border-radius:50%;position:relative}
.acc-icon::before,.acc-icon.plus::after{content:"";position:absolute;background:var(--white)}
.acc-icon::before{left:3px;top:6px;width:7px;height:1.5px}
.acc-icon.plus::after{left:6px;top:3px;width:1.5px;height:7px}
.card{position:absolute;width:320px;height:304px;background:var(--white);border-radius:2px}
.card-art{position:absolute;left:0;top:0;width:320px;height:200px;background:linear-gradient(180deg,#fafafa 0%,#e9e9e9 80%,#d8d8d8 100%)}
.play{position:absolute;left:134px;top:174px;width:52px;height:52px;border-radius:50%;background:var(--bright-teal);border:4px solid rgba(0,180,192,.3);background-clip:padding-box;display:flex;align-items:center;justify-content:center}
.play.orange{background-color:var(--orange);border-color:rgba(249,165,26,.3)}
.card-title{position:absolute;left:20px;top:246px;width:280px;text-align:center;font-size:13.5px;font-weight:600;line-height:19px;color:#333}
/* testimonial */
.quote-text{left:360px;top:2210px;width:480px;text-align:center;font-style:italic;font-size:15px;line-height:24px;color:#555}
.quote-mark{left:577px;top:2142px;width:46px;height:46px;border-radius:50%;background:var(--orange);color:var(--white);font-weight:800;font-size:24px;display:flex;align-items:center;justify-content:center}
/* footer */
.footer{position:absolute;left:0;top:2488px;width:1200px;height:514px;background:var(--footer-teal);color:var(--white)}
.f-head{position:absolute;font-size:16px;font-weight:700}
.f-text{position:absolute;font-size:13.5px;line-height:19px;white-space:nowrap}
.f-text b{font-weight:700}
.field{position:absolute;height:36px;border:1px solid var(--white);border-radius:18px;font-size:12.5px;padding:0 21px;display:flex;align-items:center}
.social{position:absolute;left:992px;display:flex;align-items:center;gap:11px;font-size:13px}
.social i{width:32px;height:32px;border-radius:50%;background:var(--social-dot);display:block}
</style>
</head>
<body>

<header class="hero">
  <div class="hero-panel"></div>
  <div class="brand" style="left:88px;top:32px"><span class="brand-dot"></span>Tembra</div>
  <h1 class="abs hero-title">VIDEO LIBRARY</h1>
  <p class="abs hero-sub">Browse our webinars, technical tutorials, and training videos</p>
  <nav class="nav">
    <span>Home</span><span>Solution</span><span>Pricing</span>
    <span>Resources <svg width="10" height="6" viewBox="0 0 10 6"><path d="M1 1l4 4 4-4" fill="none" stroke="#333" stroke-width="1.2"/></svg></span>
    <span>About <svg width="10" height="6" viewBox="0 0 10 6"><path d="M1 1l4 4 4-4" fill="none" stroke="#333" stroke-width="1.2"/></svg></span>
  </nav>
  <div class="abs hero-art" role="img" aria-label="Illustration of a hacker on a cloud stealing a folder above two laptops, with burning money and a thumbs-down sign"></div>
</header>

<section>
  <div class="abs intro-thumb" role="img" aria-label="Video thumbnail: Tip #1, follow a clean desk policy">
    <div class="play-big"><svg width="34" height="38" viewBox="0 0 34 38"><path d="M6 4l24 15L6 34z" fill="none" stroke="#fff" stroke-width="3" stroke-linejoin="round"/></svg></div>
  </div>
  <h2 class="abs intro-title">SECURITY AWARNESS VIDEO</h2>
  <p class="abs intro-text">Protecting your company begins with ensuring your employees are prepared to assist in keeping your environment safe. This will involve putting best practices and policies in place that promote security and training employees to be able to identify and avoid risks.&nbsp; Therefore, we’ve put together 7 security tips in a short (3:01 mins) security awareness video.</p>
  <div class="btn" style="left:648px;top:788px;width:120px;height:32px">GET PRICING</div>
</section>

<section class="popular">
  <h2 class="sec-title" style="top:73px">MOST POPULAR</h2>
  <div class="acc" style="top:137px">TEMBRA DATA PRIVACY<span class="acc-icon plus"></span></div>
  <div class="acc open" style="top:193px">SOCIAL NETWORKS EXPOSURE<span class="acc-icon"></span></div>

  <article class="card" style="left:88px;top:273px"><div class="card-art" role="img" aria-label="Cartoon of Milo working at a desk from home"></div><div class="play"><svg width="18" height="20" viewBox="0 0 18 20"><path d="M3 2l13 8-13 8z" fill="none" stroke="#fff" stroke-width="2" stroke-linejoin="round"/></svg></div><h3 class="card-title">MILO WORKS FROM<br>HOME</h3></article>
  <article class="card" style="left:440px;top:273px"><div class="card-art" role="img" aria-label="Cartoon of an office worker at a tidy desk"></div><div class="play orange"><svg width="18" height="20" viewBox="0 0 18 20"><path d="M3 2l13 8-13 8z" fill="none" stroke="#fff" stroke-width="2" stroke-linejoin="round"/></svg></div><h3 class="card-title">CLEAN DESK POLICY SECURITY<br>AWARENESS VIDEO</h3></article>
  <article class="card" style="left:792px;top:273px"><div class="card-art" role="img" aria-label="Cartoon of a toy unicorn representing a trojan horse"></div><div class="play"><svg width="18" height="20" viewBox="0 0 18 20"><path d="M3 2l13 8-13 8z" fill="none" stroke="#fff" stroke-width="2" stroke-linejoin="round"/></svg></div><h3 class="card-title">TEMBRA | MILO LEARNS ABOUT<br>THE TROJAN HORSE</h3></article>

  <article class="card" style="left:88px;top:609px"><div class="card-art" role="img" aria-label="Cartoon of Milo at his desk near a window"></div><div class="play"><svg width="18" height="20" viewBox="0 0 18 20"><path d="M3 2l13 8-13 8z" fill="none" stroke="#fff" stroke-width="2" stroke-linejoin="round"/></svg></div><h3 class="card-title">TEMBRA | MILO AND THE CLEAN<br>DESK POLICY</h3></article>
  <article class="card" style="left:440px;top:609px"><div class="card-art" role="img" aria-label="Cartoon of friends on a beach holiday"></div><div class="play"><svg width="18" height="20" viewBox="0 0 18 20"><path d="M3 2l13 8-13 8z" fill="none" stroke="#fff" stroke-width="2" stroke-linejoin="round"/></svg></div><h3 class="card-title">TEMBRA | MILO LEARNS ABOUT<br>PRIZE &amp; LOTTERY SCAMS</h3></article>
  <article class="card" style="left:792px;top:609px"><div class="card-art" role="img" aria-label="Cartoon of people in a café using phones"></div><div class="play"><svg width="18" height="20" viewBox="0 0 18 20"><path d="M3 2l13 8-13 8z" fill="none" stroke="#fff" stroke-width="2" stroke-linejoin="round"/></svg></div><h3 class="card-title">TEMBRA | MILO LEARNS ABOUT<br>SOCIAL MEDIA RISKS</h3></article>

  <div class="acc" style="top:946px">PHISHING AWARENESS<span class="acc-icon plus"></span></div>
  <div class="acc" style="top:1001px">SOCIAL ENGINEERING<span class="acc-icon plus"></span></div>

  <h2 class="sec-title" style="top:1123px">CLIENT TESTIMONIALS</h2>
</section>

<svg class="abs" style="left:200px;top:2150px" width="800" height="290" viewBox="0 0 800 290" aria-hidden="true">
  <defs><filter id="soft" x="-10%" y="-10%" width="120%" height="130%"><feDropShadow dx="0" dy="8" stdDeviation="10" flood-color="#000" flood-opacity=".08"/></filter></defs>
  <polygon points="40,17 760,17 745,35 593,256 205,256 53,35" fill="#fff" filter="url(#soft)"/>
  <path d="M28 128l-8 8 8 8" fill="none" stroke="#888" stroke-width="1.5"/>
  <path d="M772 128l8 8-8 8" fill="none" stroke="#888" stroke-width="1.5"/>
  <line x1="380" y1="180" x2="420" y2="180" stroke="var(--orange)" stroke-width="2"/>
</svg>
<div class="abs quote-mark">66</div>
<p class="abs quote-text">It is a long established fact that a reader will be distracted by the readable content of a page when looking at its layout. The point of using Lorem Ipsum is that it has a more-or-less normal distribution of letters, opposed to ...</p>
<div class="abs" style="left:400px;top:2341px;width:400px;text-align:center;color:var(--bright-teal);font-weight:500;font-size:15px">Lorem Ipsum dummy</div>
<div class="abs" style="left:400px;top:2363px;width:400px;text-align:center;font-size:13px;color:#333">Typesetting</div>

<footer class="footer">
  <h4 class="f-head" style="left:88px;top:80px">CONTACT US</h4>
  <p class="f-text" style="left:88px;top:114px"><b>EUROPE TEMBRA SHIELD</b><br>AG Lindenweg 12 I 6310<br>Baar I Switzerland</p>
  <p class="f-text" style="left:88px;top:198px"><b>NORTH AMERICA TEMBRA SHIELD</b><br>USA 4410 Harbor Blvd Suite 125 Denver,<br>CO 80203</p>
  <p class="f-text" style="left:88px;top:290px">Phone Global: +41 44 000 12 34<br>Phone USA: +1-555-014-2210<br>Phone USA Support: +1-555-014-2211<br>Phone Canada: +1 555-014-2290<br>Phone France: +33 600 000 118<br>Phone UK: +44 (0) 7700 900418</p>

  <h4 class="f-head" style="left:440px;top:80px">GET IN TOUCH</h4>
  <div class="field" style="left:440px;top:117px;width:236px">Enter your Name</div>
  <div class="field" style="left:692px;top:117px;width:236px">Email Address</div>
  <div class="field" style="left:440px;top:169px;width:236px">Phone</div>
  <div class="field" style="left:692px;top:169px;width:236px">Subject</div>
  <div class="field" style="left:440px;top:223px;width:488px;height:95px;align-items:flex-start;padding-top:10px;border-radius:14px">Message ...</div>
  <div class="btn" style="left:440px;top:336px;width:111px;height:35px;border-radius:18px">SUBMIT</div>

  <h4 class="f-head" style="left:992px;top:81px">LANGUAGE</h4>
  <div class="abs" style="left:992px;top:118px;width:120px;height:30px;border-radius:15px;background:#fff;color:var(--bright-teal);font-size:14px;display:flex;align-items:center;justify-content:space-between;padding:0 14px 0 16px">English <svg width="9" height="6" viewBox="0 0 9 6"><path d="M1 1l3.5 3.5L8 1" fill="none" stroke="#999" stroke-width="1.2"/></svg></div>
  <h4 class="f-head" style="left:992px;top:188px">CONNECT</h4>
  <div class="social" style="top:220px"><i></i>Circlenet</div>
  <div class="social" style="top:259px"><i></i>Chirpline</div>
  <div class="social" style="top:299px"><i></i>Vidcast</div>
  <div class="social" style="top:339px"><i></i>Worklink</div>

  <div class="abs" style="left:88px;top:421px;width:1024px;height:1px;background:rgba(255,255,255,.6)"></div>
  <div class="brand" style="left:0;width:1200px;justify-content:center;top:447px;font-size:20px;gap:6px"><span class="brand-dot" style="width:20px;height:20px"></span>Tembra</div>
  <p class="abs" style="left:0;width:1200px;text-align:center;top:479px;font-size:12.5px">All Rights Reserved 2021</p>
</footer>

</body>
</html>
```